Lens Harbor Teutonia Website - Photography and Films

We are looking for a design that expresses the friendly, open nature of our company Lens Harbor Teutonia, yet at the same time is professional looking and functional.

Lens Harbor Teutonia is a B2B focused operation that hires out multi-lingual camera crews (and equipment) throughout Germany and Europe. We also produce tv features and coporate films. Our unique selling point is that we are native English speakers who can communicate with our international clients (usually British or American) and organise the logistics of shooting in foreign countries.

For content inspiration, see our current website: http://www.lensharborteutonia.com - however we want to move away from the very simple structure of this site and move towards a layout that displays and allows for frequently updated content (e.g. in the form of a blog).

Here is an example of the kind of clean look we like:
http://www.qrvpixelarchive.com/archive/main/reelsqrv.do#reel=48213760

Please keep within the following specifications:
- We wish to keep our logo (grey/white, font: Glypha) and our company colour red (#C40A0A) as they are.
- Maximum Width 960px, on a large browser-window the design should be centred
- Easily readable font sizes with good contrast
- Provide your design in PSD file format
- Our logo should be graphically displayed in the top left of the header.
- The design should allow space for a video.
- The page should have a clearly recognisable end in the form of a footer.

The following menu items need to be clearly arranged so the viewer is not overwhelmed or confused:
About
Services - Crews / Corporate Shoots / Webcasts / Production Arm / Legal Videography
Recent Productions
Blog
Testimonials
Get a Quote
Contact
Film Library
Showreel
Events
Film Location Guide - Frankfurt / Cologne / Zurich / Helsinki / Amsterdam / London / Paris / Rome / Brussels / Berlin / Munich
Updates

Reason: Hi - thanks very much for your interest in our design project.  We are extending this auction because we haven't had enough time to really focus on the desigs and provide immediate feedback to designers.  We will try to provide timely feedback and are giving you more time to make any adjustments to your designs etc.
Thanks!
Marla

Target Market(s)

Our target customers are males and females between 25 and 55 years (mostly British and American). More important than their demographic though, is their occupation - they are largely communication and design savvy individuals belonging to one of the following three categories: 1)Broadcasters (usually producers for example from the QRV or Horizon Vista TV seeking trustworthy, affordable crews for their foreign shoots).

2) Video Production Companies (seeking a trustworthy, affordable partner company to provide the crews for their own corporate clients).

3) Corporate Communications Specialists (seeking professional producers and crews to facilitate production of company videos or filming of events).

Industry/Entity Type

Camera

Requirements
Must have
• A fresh clean appearance with good use of white space.
Should not have
• Avoid dark heavy colours and designs.
• Avoid designs that would be impractical and could potentially take a long time to load.

```html
<!DOCTYPE html>
<html lang="en">
<head>
<meta charset="utf-8">
<title>Lens Harbor Teutonia</title>
<link href="https://fonts.googleapis.com/css2?family=Roboto+Slab:wght@700&family=PT+Sans+Narrow&family=PT+Sans:wght@400;700&display=swap" rel="stylesheet">
<style>
:root{
  --brand-red:#c40a0a;
  --header-red:#b8262b;
  --video-red:#c82f3d;
  --page-pink:#e99a9c;
  --grey-light:#e4e5e8;
  --grey-mid:#b7b9be;
  --grey-dark:#6e7076;
  --text:#444;
  --white:#fff;
}
*{box-sizing:border-box;margin:0;padding:0}
html,body{width:1200px;height:960px;overflow:hidden}
body{position:relative;font-family:"PT Sans",sans-serif;color:var(--text);
  background:radial-gradient(circle at 20% 30%,#f6c9c9 0,#e99a9c 45%,#e38d90 100%)}
.abs{position:absolute}
.frame{left:148px;top:28px;width:901px;height:899px;background:var(--white);border:1px solid #ddd}
.header{left:150px;top:30px;width:897px;height:90px;background:linear-gradient(#a51e23,var(--header-red) 30%,#c0373b)}
.header-strip{left:150px;top:120px;width:897px;height:10px;background:linear-gradient(#ccc,#a9abb0)}
.logo{font-family:"Roboto Slab",serif;font-weight:700;color:var(--white);font-size:32px;letter-spacing:-.5px}
.header .logo{position:absolute;left:44px;top:36px}
.nav{left:582px;top:94px;display:flex;height:26px;font-family:"PT Sans Narrow",sans-serif;font-size:14px}
.nav a{color:var(--white);text-decoration:none;padding:4px 6px;border-right:1px solid #d46a6d;white-space:nowrap}
.nav a.active{background:linear-gradient(#fafafa,#d9d9d9);color:#777;border-radius:2px 2px 0 0}
.flag{width:14px;height:9px;margin:7px 0 0 12px;background:linear-gradient(#222 33%,#d00 33% 66%,#fc0 66%)}
.sidebar{left:160px;top:143px;width:140px;height:397px;border:1px solid var(--brand-red);border-right-width:2px;background:var(--white);font-family:"PT Sans Narrow",sans-serif;font-size:13px}
.menu-item{height:23.5px;line-height:22px;padding-left:14px;color:#555;background:linear-gradient(#eceef1,#b9bbc1);border-bottom:1px solid #fff;position:relative}
.menu-item.open::after,.menu-item.more::after{content:"";position:absolute;right:6px;top:8px;border:6px solid transparent;border-top-color:var(--brand-red);border-bottom:0}
.sub-item{height:23.5px;line-height:23px;padding-left:44px;color:#555}
.sub-list{height:140px;padding-top:2px}
.follow{left:190px;top:797px;font-size:8px;color:#333}
.social{top:812px;width:31px;height:31px;border-radius:5px;color:#fff;font-size:7px;display:flex;align-items:center;justify-content:center}
.divider-v{left:298px;top:143px;height:719px;border-left:1px dotted #bbb}
.divider-h{left:302px;top:503px;width:535px;border-top:1px dotted #bbb}
.divider-top{left:302px;top:143px;width:535px;border-top:1px dotted #bbb}
.player{left:314px;top:159px;width:514px;height:329px;background:linear-gradient(135deg,#d9d9d9,#f4f4f4 40%,#c9c9c9);border-radius:2px}
.screen{left:15px;top:13px;width:484px;height:293px;background:var(--video-red)}
.screen .logo{position:absolute;left:73px;top:128px;font-size:33px}
.play{left:226px;top:139px;width:32px;height:32px;background:#7a1820;border-radius:3px}
.controls{left:15px;top:306px;width:484px;height:14px;background:linear-gradient(#fff,#ddd);border:1px solid #999;font-size:7px;font-weight:700;display:flex;align-items:center;gap:5px;padding:0 4px}
.track{flex:1;height:3px;background:#999}
.intro{left:315px;top:509px;width:516px;font-size:11.3px;line-height:12.3px;color:#444}
.intro p{margin-bottom:13px}
.intro ul{padding-left:13px}
.team-photo{left:380px;top:665px;width:420px;height:197px;background:linear-gradient(90deg,#fff,#bfc3c8 20%,#6c6f76 55%,#aeb2b8 85%,#fff);border-radius:80px 80px 0 0}
.library{left:840px;top:143px;width:198px;height:719px;border:1px solid var(--brand-red);background:var(--grey-light);overflow:hidden}
.library-head{height:46px;background:linear-gradient(#f5f5f6,#a5a7ad);color:#fff;font-weight:700;font-size:19px;text-align:center;line-height:46px;text-shadow:0 1px 2px #666}
.scrollbar{right:0;top:46px;width:14px;height:673px;background:#f0f0f0}
.scroll-thumb{left:2px;top:14px;width:10px;height:68px;background:#c9cbd0;border-radius:3px}
.film{position:absolute;left:0;width:182px;background:var(--white);border-bottom:1px dotted #aaa;padding:0 8px}
.thumb{margin:12px 0 0 19px;width:131px;height:96px;position:relative}
.thumb::after{content:"";position:absolute;left:62px;top:41px;border:7px solid transparent;border-left:10px solid #fff;border-right:0}
.film h3{font-size:9.5px;margin-top:4px;color:#555}
.film p{font-size:7px;line-height:8.5px;color:#444}
.footer{left:150px;top:862px;width:897px;height:64px;background:linear-gradient(#b0b2b8 0,#b0b2b8 5%,var(--header-red) 5%,#a8232a)}
.footer .logo{position:absolute;left:78px;top:13px;font-size:22px}
.footer-info{left:330px;top:21px;color:#fff;font-size:8.6px;font-weight:700;line-height:10px}
</style>
</head>
<body>
<div class="abs frame"></div>

<header class="abs header">
  <div class="logo">Lens Harbor Teutonia</div>
</header>
<nav class="abs nav">
  <a class="active">home</a><a>showreel</a><a>production arm</a><a>legal videography</a><a>legal videography</a><a style="border:0">contact</a>
  <span class="flag"></span>
</nav>
<div class="abs header-strip"></div>

<aside class="abs sidebar">
  <div class="menu-item">About Us</div>
  <div class="menu-item open">Services</div>
  <div class="sub-list">
    <div class="sub-item">Crews</div>
    <div class="sub-item">Corporate Shoots</div>
    <div class="sub-item">Webcasts</div>
    <div class="sub-item">Production Arm</div>
    <div class="sub-item">Legal Videography</div>
  </div>
  <div class="menu-item more">Recent Productions</div>
  <div class="menu-item">Blog</div>
  <div class="menu-item more">Testimonials</div>
  <div class="menu-item">Get a Quote</div>
  <div class="menu-item">Contact&nbsp; Us</div>
  <div class="menu-item">Film Library</div>
  <div class="menu-item">Showreel</div>
  <div class="menu-item">Events</div>
  <div class="menu-item more">Film Location Guide</div>
</aside>
<div class="abs follow">Follow us on</div>
<div class="abs social" style="left:190px;background:#3fb4e0">Chirpline</div>
<div class="abs social" style="left:231px;background:#3b5a9a">Friendsbook</div>

<div class="abs divider-v"></div>
<div class="abs divider-top"></div>

<section class="abs player">
  <div class="abs screen">
    <div class="logo">Lens Harbor Teutonia</div>
    <svg class="abs play" viewBox="0 0 32 32"><path d="M12 9l11 7-11 7z" fill="#fff"/></svg>
  </div>
  <div class="abs controls"><span>▶</span><span>■</span><span>00:00</span><span class="track"></span><span>03:03</span><span>⛶</span><span>◂‖‖</span></div>
</section>

<div class="abs divider-h"></div>

<section class="abs intro">
  <p>We set up Lens Harbor Teutonia to meet the demands of a growing number of TV-producers whose working language is English. This is our Passion! Why else would we keep doing it for over 30 years!</p>
  <p>As a producer, you're bound to have great ideas...but how do you make them a reality in a country where you can't speak the language? Partner with us! We are native English speakers so nothing gets lost in translation. We'll catch hold of your vision, and with local know-how, we'll make it happen. No job is too big, too small, too hard, too far away, or too urgent. Try us!</p>
  <ul>
    <li>We provide camera crews and facilities throughout Germany and Europe</li>
    <li>We shoot in both PAL and NTSC</li>
    <li>We edit either in-studio or on the move and we transfer urgent footage via FTP or SNG</li>
    <li>We are on call 24/7</li>
  </ul>
</section>
<div class="abs team-photo" role="img" aria-label="Group photo of the production team in business attire"></div>

<aside class="abs library">
  <div class="library-head">Film Library</div>
  <div class="film" style="top:46px;height:187px">
    <div class="thumb" role="img" aria-label="Video still: young girl in a clinic" style="background:linear-gradient(#5b4a35,#2a2219)"></div>
    <h3>Children in pain</h3>
    <p>We portray Anton Feldmark and his pioneering treatment for children with terminal illnesses who suffer great pain.</p>
  </div>
  <div class="film" style="top:234px;height:190px">
    <div class="thumb" role="img" aria-label="Video still: police officers in a corridor" style="background:linear-gradient(90deg,#c4773a,#3a3a40 40%,#8a8c92)"></div>
    <h3>Burglar prevention</h3>
    <p>German police introduced an innovative method of tracking down burglars by coating valuables with an artificial and invisible DNA. Burglary suspects can then be scanned to see if they have been in contact with the stolen goods.</p>
  </div>
  <div class="film" style="top:425px;height:197px">
    <div class="thumb" role="img" aria-label="Video still: crowd in a beer hall" style="background:linear-gradient(#8a6a45,#4a3a2c)"></div>
    <h3>Political situation, Germany</h3>
    <p>The recession hit the German economy badly in 2009. One way to cope with situation was the shorter working week otherwise known as "Kurzarbeit".</p>
  </div>
  <div class="film" style="top:623px;height:96px">
    <div class="thumb" role="img" aria-label="Video still: crowded street scene" style="background:linear-gradient(#3a3a34,#5a5040)"></div>
  </div>
  <div class="abs scrollbar">
    <svg class="abs" style="left:2px;top:2px" width="10" height="6"><path d="M0 6L5 0l5 6z" fill="#c40a0a"/></svg>
    <div class="abs scroll-thumb"></div>
    <svg class="abs" style="left:2px;bottom:2px" width="10" height="6"><path d="M0 0l5 6 5-6z" fill="#c40a0a"/></svg>
  </div>
</aside>

<footer class="abs footer">
  <div class="logo">Lens Harbor Teutonia</div>
  <div class="abs footer-info">c/o Kellwen Studios • Lindenweg 12 • 60311 Frankfurt/Main • Germany • hello@lensharborteutonia.com<br>Tel.: +49-69-000000 • Toll free from the USA 1-800-555-0147<br>Disclaimer</div>
</footer>
</body>
</html>
```